Political themed graphic for contemporary church sermon series

Contemporary church in California need a graphic design for a sermon series. The sermon series will be focused on the upcoming presidential election. The sermon series is titled for the question "who will be the next president":

Title: 45
Subtitle: Who will it be / Does it matter

The design should use red, white and blue and should possibly have the amber lodge in the graphic somewhere. Maybe like a watermark or something to that effect.

Target Market(s)

Contemporary design,

Industry/Entity Type

Church

Font styles to use
Serif
Sans Serif

Colors
0555a3
ec1f27
ffffff

Requirements
Must have
• Political theme, red, white and blue (contemporary color palette). Amber lodge screened back in the design somewhere.
• the title large: 45
• and subtitle: Who will it be | Does it matter
Should not have
• I'm not looking for cheesy graphics with elephant and a donkey.

```html
<!DOCTYPE html>
<html lang="en">
<head>
<meta charset="utf-8">
<title>45 — Who Will Be The Next President</title>
<link href="https://fonts.googleapis.com/css2?family=Montserrat:wght@600;700;800&display=swap" rel="stylesheet">
<style>
  :root {
    --blue-deep: #1c0f8a;
    --blue: #2d1fc2;
    --blue-bright: #4a3cf0;
    --red: #c8101e;
    --red-deep: #7d0610;
    --red-dark: #3a0206;
    --white: #ffffff;
    --stone: #e9ecef;
  }
  html, body {
    margin: 0;
    padding: 0;
    width: 1200px;
    height: 1200px;
    overflow: hidden;
    background: var(--white);
  }
  .canvas {
    position: relative;
    width: 1200px;
    height: 1200px;
  }
  .poster {
    position: absolute;
    left: 242px;
    top: 102px;
    width: 700px;
    height: 990px;
    overflow: hidden;
    font-family: "Montserrat", sans-serif;
    color: var(--white);
    background: var(--red-deep);
  }
  .sky {
    position: absolute;
    inset: 0 0 auto 0;
    height: 320px;
    background:
      radial-gradient(circle at 80% 20%, rgba(120,110,255,.45), transparent 40%),
      radial-gradient(circle at 15% 60%, rgba(90,80,255,.35), transparent 45%),
      linear-gradient(180deg, var(--blue-deep) 0%, var(--blue) 60%, var(--blue-bright) 100%);
  }
  .landmark {
    position: absolute;
    left: 0;
    top: 282px;
    width: 700px;
    height: 460px;
    background:
      linear-gradient(180deg, rgba(255,255,255,0) 0%, rgba(255,255,255,0) 80%, var(--red) 100%),
      linear-gradient(165deg, var(--blue) 0%, #5a4fd8 14%, var(--white) 28%, var(--red) 34%, var(--white) 42%, var(--stone) 60%, var(--white) 80%);
  }
  .ground {
    position: absolute;
    left: 0;
    top: 722px;
    width: 700px;
    height: 268px;
    background: radial-gradient(circle at 50% 0%, var(--red) 0%, #a80a16 55%, var(--red-deep) 100%);
  }
  .kicker {
    position: absolute;
    top: 32px;
    width: 100%;
    text-align: center;
    font-weight: 700;
    font-size: 22px;
    letter-spacing: 6px;
    margin: 0;
  }
  .headline {
    position: absolute;
    top: 62px;
    width: 100%;
    margin: 0;
    text-align: center;
    font-weight: 700;
    line-height: 1;
    text-shadow: 0 3px 10px rgba(0,0,0,.35);
  }
  .headline .line-1 { display: block; font-size: 88px; letter-spacing: -1px; }
  .headline .line-2 { display: block; font-size: 114px; letter-spacing: -2px; margin-top: 10px; }
  .series-number {
    position: absolute;
    left: 40px;
    top: 280px;
    width: 620px;
    height: 420px;
  }
  .series-number text {
    font-family: "Montserrat", sans-serif;
    font-weight: 800;
    font-size: 520px;
    letter-spacing: -20px;
  }
  .portrait {
    position: absolute;
    left: 0;
    top: 754px;
    width: 146px;
    height: 236px;
    background: var(--red-dark);
    border: 6px solid var(--white);
    border-left: none;
    border-bottom: none;
    border-radius: 0 70px 0 0;
    box-sizing: border-box;
  }
  .subtitle {
    position: absolute;
    left: 160px;
    top: 800px;
    margin: 0;
    font-weight: 800;
    font-size: 52px;
    line-height: 1.15;
    letter-spacing: -0.5px;
    text-shadow: 0 3px 8px rgba(0,0,0,.4);
  }
  .subtitle span { display: block; }
  .question-mark {
    position: absolute;
    left: 614px;
    top: 788px;
    font-weight: 800;
    font-size: 140px;
    line-height: 1;
    text-shadow: 0 3px 8px rgba(0,0,0,.4);
  }
</style>
</head>
<body>
<div class="canvas">
  <section class="poster">
    <div class="sky" role="img" aria-label="Starry deep blue night sky"></div>
    <div class="landmark" role="img" aria-label="Photo of the Amber Lodge with a waving flag above it"></div>
    <div class="ground"></div>

    <p class="kicker">WHO WILL BE</p>
    <h1 class="headline">
      <span class="line-1">THE NEXT</span>
      <span class="line-2">PRESIDENT</span>
    </h1>

    <svg class="series-number" viewBox="0 0 620 420" aria-label="45">
      <defs>
        <linearGradient id="numberFill" x1="0" y1="0" x2="0" y2="1">
          <stop offset="0" stop-color="#d8121f"/>
          <stop offset="1" stop-color="#9c0714"/>
        </linearGradient>
        <filter id="numberShadow" x="-10%" y="-10%" width="120%" height="120%">
          <feDropShadow dx="0" dy="6" stdDeviation="8" flood-color="#000" flood-opacity=".35"/>
        </filter>
      </defs>
      <text x="300" y="390" text-anchor="middle" fill="url(#numberFill)"
            stroke="#ffffff" stroke-width="16" paint-order="stroke"
            stroke-linejoin="round" filter="url(#numberShadow)">45</text>
    </svg>

    <div class="portrait" role="img" aria-label="Silhouette of an unknown candidate"></div>

    <h2 class="subtitle">
      <span>WHO WILL IT BE</span>
      <span>DOES IT MATTER</span>
    </h2>
    <div class="question-mark">?</div>
  </section>
</div>
</body>
</html>
```